Psychologist website

Simple psychologist website
Site map:
home
self-test
common conditions
children
contact
about
info

Current website:
http://www.corvalepsychology.com.au/

Not in love with logo, or colours etc - open brief
Happy for new font/style/logo for company name

Customer wants clean, credible and warm and friendly look & feel
stock photos OK

Brief:

One home page - simple with 2 or 3 small areas to tease and attract the user and one template page to suit all the other pages

Pages structurally similar to
http://www.wendlecourt.com.au/
In that the home page is different and the other pages are based on one template

Requirements
Must have
• 2 pages - one home page and one template page
• navigation for site map

```html
<!DOCTYPE html>
<html lang="en">
<head>
<meta charset="utf-8">
<title>Corvale &amp; Associates — Clinical Psychologists</title>
<link rel="stylesheet" href="https://fonts.googleapis.com/css2?family=PT+Sans:ital,wght@0,400;0,700;1,400&family=Roboto+Condensed:wght@300;400&display=swap">
<style>
:root{
  --blue:#0a86b5;
  --blue-dark:#07719a;
  --blue-deep:#0b6d92;
  --ink:#555a5e;
  --ink-dark:#3e4346;
  --line:#e4e6e8;
  --nav-bg:#f7f8f8;
  --white:#ffffff;
}
*{box-sizing:border-box;margin:0;padding:0}
html,body{width:1200px;height:972px;overflow:hidden;background:var(--white)}
body{position:relative;font-family:"PT Sans",sans-serif;color:var(--ink)}
.abs{position:absolute}
.top-band{left:0;top:0;width:1200px;height:7px;background:var(--blue)}

.brand{left:175px;top:31px;color:var(--blue-deep);font-weight:400;text-transform:uppercase;line-height:1;white-space:nowrap}
.brand .name{font-size:23px;letter-spacing:1.2px;display:block}
.brand .tag{font-size:15px;letter-spacing:2.9px;display:block;margin-top:11px}

.call{left:770px;top:37px}
.call svg{position:absolute;left:0;top:0}
.call .num{position:absolute;left:44px;top:3px;white-space:nowrap;color:var(--blue);font-weight:700;font-size:13px}
.call .note{position:absolute;left:46px;top:25px;white-space:nowrap;color:var(--ink-dark);font-weight:700;font-size:10.5px;text-transform:uppercase}

.main-nav{left:175px;top:109px;width:845px;height:37px;background:var(--nav-bg);border:1px solid var(--line)}
.main-nav a{position:absolute;top:12px;font-size:10.5px;font-weight:700;color:var(--ink);text-decoration:none;text-transform:uppercase;white-space:nowrap}
.main-nav a.active{color:var(--blue)}
.search{left:651px;top:6px;width:182px;height:20px;background:#fff;border:1px solid #d9dcdf}
.search span{position:absolute;left:11px;top:5px;font-size:7.5px;color:#8a8f93;text-transform:uppercase}
.search svg{position:absolute;right:8px;top:4px}

.hero-photo{left:175px;top:154px;width:586px;height:361px;background:linear-gradient(100deg,#e9eaea 0%,#c9c8c3 30%,#8c7c68 50%,#5b5a58 75%,#8e9296 100%)}
.hero-panel{left:761px;top:154px;width:259px;height:361px;background:var(--blue);color:var(--white)}
.hero-panel .fold{position:absolute;right:0;top:0}
.hero-panel h1{position:absolute;left:29px;top:50px;font-family:"Roboto Condensed",sans-serif;font-weight:400;line-height:1.15;white-space:nowrap}
.hero-panel h1 small{display:block;font-size:19px}
.hero-panel h1 span{display:block;font-size:25px;line-height:1.15;letter-spacing:-0.2px}
.hero-panel p{position:absolute;left:30px;top:144px;font-family:"Roboto Condensed",sans-serif;font-weight:300;font-size:20px;line-height:24px;letter-spacing:-0.4px;white-space:nowrap}
.hero-arrows{left:950px;top:472px}
.hero-arrows span{position:absolute;top:0;width:26px;height:26px;background:#2a7d9e;display:block}

.section-title{font-family:"PT Sans",sans-serif;font-weight:700;font-size:15.5px;color:var(--blue);text-transform:uppercase;white-space:nowrap}
.about-title{left:175px;top:544px}
.about-photo{left:175px;top:582px;width:184px;height:108px;background:linear-gradient(90deg,#e8ecef,#bcc6cf 45%,#c7a890 75%,#e6e3df)}
.about-text{left:383px;top:578px;font-size:9.2px;line-height:15.5px;letter-spacing:-0.15px;color:var(--ink);white-space:nowrap}
.btn{left:384px;top:666px;width:92px;height:24px;background:var(--blue);color:#fff;font-size:9px;font-weight:700;text-transform:uppercase;text-align:center;line-height:24px;border:1px solid var(--blue-dark)}

.divider{left:832px;top:539px;width:2px;height:323px;background:#eeeff0}

.side-menu{left:855px;top:546px;width:162px;list-style:none}
.side-menu li{height:26px;line-height:26px;padding-left:14px;font-size:8.6px;text-transform:uppercase;color:var(--ink-dark);border-bottom:1px solid #eceeef;white-space:nowrap}
.side-menu li.active{background:var(--blue);color:#fff;font-weight:700;border-bottom:none}

.staff-title{left:175px;top:721px}
.staff-arrows{left:781px;top:722px}
.staff-arrows span{position:absolute;top:0;width:16px;height:16px;background:#eceeef}
.staff-card{top:760px;width:220px}
.staff-card .photo{position:absolute;left:0;top:0;width:72px;height:76px;border:3px solid #e6e8ea;background:linear-gradient(180deg,#e9ecef,#c9b8a6 55%,#dfe3e6)}
.staff-card .info{position:absolute;left:85px;top:0;width:140px;white-space:nowrap}
.staff-card h3{font-size:10.5px;font-weight:700;color:var(--blue);text-transform:uppercase}
.staff-card .quals{font-size:9.5px;font-style:italic;color:var(--blue);margin-top:4px;padding-left:2px}
.staff-card p{font-size:9.5px;line-height:15.5px;color:var(--ink);margin-top:3px;padding-left:2px}
.staff-card .offices{color:var(--blue)}

.footer-rule{left:175px;top:884px;width:845px;height:4px;background:#eceeef}
.footer-nav{left:184px;top:909px;font-size:8px;text-transform:uppercase;color:var(--ink-dark);white-space:nowrap}
.footer-nav span{margin:0 9px}
.copy{left:184px;top:930px;font-size:8px;text-transform:uppercase;color:var(--ink-dark);white-space:nowrap}
.copy em{font-style:normal;color:var(--blue)}
.follow{left:860px;top:920px;font-size:8px;text-transform:uppercase;color:var(--ink-dark);white-space:nowrap}
.social{top:910px;width:27px;height:27px;border-radius:50%}
</style>
</head>
<body>
<div class="abs top-band"></div>

<div class="abs brand"><span class="name">Corvale &amp; Associates</span><span class="tag">Clinical Psychologists</span></div>

<div class="abs call">
  <svg width="38" height="38" viewBox="0 0 38 38">
    <rect x="1" y="1" width="36" height="36" rx="5" fill="#4aa3d6" stroke="#2f86bd"/>
    <path d="M12 9c-2 1-3 3-2 6 2 6 7 11 13 13 3 1 5 0 6-2l-4-4-3 2c-3-1-6-4-7-7l2-3z" fill="#fff"/>
  </svg>
  <div class="num">CALL US : 98110452</div>
  <div class="note">For all appointments and enquiries.</div>
</div>

<nav class="abs main-nav">
  <a class="active" style="left:26px">Home</a>
  <a style="left:109px">Services Offered</a>
  <a style="left:249px">FAQ</a>
  <a style="left:321px">Our Staff</a>
  <a style="left:425px">Appointments</a>
  <a style="left:551px">Contact Us</a>
  <div class="abs search"><span>Search :</span>
    <svg width="14" height="12" viewBox="0 0 14 12"><circle cx="5" cy="5" r="3.5" fill="none" stroke="#9aa0a4" stroke-width="1.5"/><path d="M7.5 7.5l5 3.5" stroke="#9aa0a4" stroke-width="2"/></svg>
  </div>
</nav>

<div class="abs hero-photo" role="img" aria-label="Stock photo of a stressed woman at her office desk holding her head"></div>
<section class="abs hero-panel">
  <svg class="fold" width="26" height="26" viewBox="0 0 26 26"><path d="M0 0H26V26Z" fill="#fff"/><path d="M0 0V26H26Z" fill="#0b6186"/></svg>
  <h1><small>Welcome to</small><span>Corvale &amp; Associates</span><span>Clinical Psychologists</span></h1>
  <p>Psychologists, in Sydney,<br>Chatswood, and Westmead.<br>We provide expert treatment<br>for depression, anxiety,<br>eating disorders and other<br>issues.</p>
</section>
<div class="abs hero-arrows">
  <span style="left:0"><svg width="26" height="26"><path d="M15 8l-5 5 5 5" fill="none" stroke="#9fc6d8" stroke-width="2"/></svg></span>
  <span style="left:30px"><svg width="26" height="26"><path d="M11 8l5 5-5 5" fill="none" stroke="#9fc6d8" stroke-width="2"/></svg></span>
</div>

<h2 class="abs section-title about-title">About Corvale Psychology</h2>
<div class="abs about-photo" role="img" aria-label="Stock photo of a doctor in a consultation with a client"></div>
<p class="abs about-text">Our psychologists provide a comfortable, supportive, and confidential environment for their clients. Our first<br>goal is for you to feel comfortable in exploring issues and sharing sharing your concerns, knowing that you<br>have been heard and understood. It is in this kind of environment that client and therapist can work<br>produchave been heard and understood. It is in this kind of environment that client and therapist can work<br>productively to understand problems and seek solutions.</p>
<div class="abs btn">Read More</div>

<div class="abs divider"></div>

<ul class="abs side-menu">
  <li class="active">Mood</li>
  <li>Anxiety</li>
  <li>Physical Health</li>
  <li>Eating Disorders</li>
  <li>Physical Health</li>
  <li>Infant and Child Services</li>
  <li>Trauma</li>
  <li>ADHD</li>
  <li>Psychometric Assessment</li>
  <li>Addictions</li>
  <li>Stress</li>
  <li>Skills to Enhance Your Life</li>
</ul>

<h2 class="abs section-title staff-title">Our Staff</h2>
<div class="abs staff-arrows"><span style="left:0"></span><span style="left:19px"></span></div>

<article class="abs staff-card" style="left:175px">
  <div class="photo" role="img" aria-label="Portrait photo of a staff psychologist"></div>
  <div class="info"><h3>Dr Alan Merrow</h3><div class="quals">B.A. (Hons); M.Psychol.; PhD</div><p>Alan sees clients at the<br>following offices:<br><span class="offices">Westmead, Chatswood, City</span></p></div>
</article>
<article class="abs staff-card" style="left:401px">
  <div class="photo" role="img" aria-label="Portrait photo of a staff psychologist"></div>
  <div class="info"><h3>Priya Nandal</h3><div class="quals">B.A. (Hons); M.Psychol.; PhD</div><p>Priya sees clients at the<br>following offices:<br><span class="offices">Chatswood</span></p></div>
</article>
<article class="abs staff-card" style="left:617px">
  <div class="photo" role="img" aria-label="Portrait photo of a staff psychologist"></div>
  <div class="info"><h3>Dr Lena Voss</h3><div class="quals">B.A. (Hons); M.Psychol.; PhD</div><p>Lena sees clients at the<br>following offices:<br><span class="offices">Chatswood</span></p></div>
</article>

<div class="abs footer-rule"></div>
<div class="abs footer-nav">Home<span>|</span>Services Offered<span>|</span>FAQ<span>|</span>Our Staff<span>|</span>Appointments<span>|</span>Contact Us</div>
<div class="abs copy">Copyrights © 2013. <em>Corvale Psychology</em>. All rights reserved</div>
<div class="abs follow">Follow us :</div>
<div class="abs social" style="left:916px;background:#2f6fb3" role="img" aria-label="Social link"></div>
<div class="abs social" style="left:947px;background:#3fa3dc" role="img" aria-label="Social link"></div>
<div class="abs social" style="left:978px;background:#1e77a6" role="img" aria-label="Social link"></div>
</body>
</html>
```